Wireless internet service provider needs flyer to lease property to build new tower sites

We need a flyer to leave behind at customer sites that we would like to turn into a tower location. We want to lease roof space or property from the customer to expand our network. We would like it to read as a sales ad that they can make up to $200/mo in exchange for signing a lease agreement with us. Attached are example photos of what typical residential tower sites look like. Contact number 530-647-1185 and email sales@brivolta.net. This will be left behind at a customer site, after a technician visits. It will be used as sales/marketing material. The flyer should be a 6x11 postcard.
Text to add to the flyer are the following points.
- Earn passive income
- Help your community get better internet
- We pay for all build costs

Target Market(s)

Rural residences

Industry/Entity Type

Internet Services

Requirements
Must have
• Sales pitch of "get paid up to $300/mo to host wireless equipment for our local rural ISP"

```html
<!DOCTYPE html>
<html lang="en">
<head>
<meta charset="utf-8">
<title>Brivolta.net – Host Wireless Equipment</title>
<link rel="stylesheet" href="https://fonts.googleapis.com/css2?family=Open+Sans:ital,wght@0,700;0,800;1,700&family=Ubuntu:wght@500;700&display=swap">
<style>
  :root {
    --green: #5fb21e;
    --gold: #f6c324;
    --orange: #f0a432;
    --cream: #f7f0cf;
    --white: #ffffff;
    --red: #c41414;
    --ink: #111111;
  }
  * { margin: 0; padding: 0; box-sizing: border-box; }
  html, body { width: 1200px; height: 2199px; overflow: hidden; background: var(--white); }
  .flyer { position: relative; width: 1200px; height: 2199px; overflow: hidden; font-family: "Open Sans", sans-serif; }

  .hero-photo {
    position: absolute; left: 0; top: 150px; width: 1200px; height: 1762px;
    background: linear-gradient(180deg, #2f63d0 0%, #3c78dc 30%, #6f9ee2 55%, #c9d8ee 68%, #8aa3b8 76%, #3f5a3a 82%, #2f4a2a 100%);
  }
  .equipment-photo {
    position: absolute; left: 640px; top: 160px; width: 560px; height: 1752px;
    background: linear-gradient(90deg, rgba(240,244,250,0) 0%, rgba(235,240,248,0.35) 45%, rgba(210,215,225,0.45) 100%);
  }

  .top-banner { position: absolute; left: 0; top: 0; width: 1200px; height: 260px; }
  .top-banner svg { position: absolute; left: 0; top: 0; }
  .top-banner h1 {
    position: absolute; left: 0; top: 10px; width: 1200px; text-align: center;
    font-family: "Ubuntu", sans-serif; font-weight: 700; font-size: 104px; line-height: 1;
    color: var(--white); letter-spacing: 1px;
  }

  .pitch { position: absolute; left: 110px; top: 262px; }
  .pitch-lead { font-weight: 800; font-size: 94px; line-height: 1; color: var(--white); letter-spacing: 1px; }
  .pitch-amount { font-weight: 800; font-size: 178px; line-height: 1; color: var(--gold); letter-spacing: -4px; }
  .pitch-detail { font-weight: 700; font-style: italic; font-size: 86px; line-height: 87px; color: var(--cream); margin-top: 8px; }

  .brand-name {
    position: absolute; left: 110px; top: 1078px;
    font-weight: 800; font-size: 92px; line-height: 1; color: var(--ink); letter-spacing: 2px;
  }

  .community { position: absolute; left: 0; top: 0; color: var(--orange); font-weight: 800; line-height: 1; }
  .community span { position: absolute; left: 110px; white-space: nowrap; }
  .community .c-help { top: 1378px; font-size: 70px; letter-spacing: 0; }
  .community .c-community { top: 1444px; font-size: 62px; letter-spacing: -2px; }
  .community .c-get { top: 1490px; font-size: 212px; letter-spacing: -6px; left: 112px; }
  .community .c-better { top: 1668px; font-size: 108px; letter-spacing: -2px; }
  .community .c-internet { top: 1758px; font-size: 80px; letter-spacing: -1px; }

  .cost-band {
    position: absolute; left: 0; top: 1910px; width: 1200px; height: 130px; background: var(--green);
    font-family: "Ubuntu", sans-serif; font-weight: 700; font-size: 92px; color: var(--white);
    text-align: center; line-height: 130px;
  }

  .contact-band { position: absolute; left: 0; top: 2052px; width: 1200px; height: 147px; background: var(--red); }
  .contact-item { position: absolute; top: 0; height: 147px; display: flex; align-items: center; gap: 22px;
    color: var(--white); font-weight: 700; font-size: 46px; }
  .contact-phone { left: 48px; }
  .contact-email { left: 570px; gap: 32px; }
</style>
</head>
<body>
<main class="flyer">
  <div class="hero-photo" role="img" aria-label="Photo of a blue sky with white clouds over a forested rural valley, seen from a rooftop"></div>
  <div class="equipment-photo" role="img" aria-label="Photo of a white rooftop mast carrying wireless radios and a dish antenna"></div>

  <header class="top-banner">
    <svg width="1200" height="260" viewBox="0 0 1200 260" aria-hidden="true">
      <path d="M0 0 H1200 V160 H440 L372 250 L304 160 H0 Z" fill="var(--gold)"/>
      <path d="M12 0 H1188 V148 H426 L372 222 L318 148 H12 Z" fill="var(--green)"/>
    </svg>
    <h1>Earn passive income</h1>
  </header>

  <section class="pitch">
    <p class="pitch-lead">GET PAID UP TO</p>
    <p class="pitch-amount">$300/mo</p>
    <p class="pitch-detail">to host wireless<br>equipment<br>for our local<br>rural ISP</p>
  </section>

  <p class="brand-name">BRIVOLTA.NET</p>

  <p class="community">
    <span class="c-help">HELP YOUR</span>
    <span class="c-community">COMMUNITY</span>
    <span class="c-get">GET</span>
    <span class="c-better">BETTER</span>
    <span class="c-internet">INTERNET</span>
  </p>

  <p class="cost-band">We pay for all build costs</p>

  <footer class="contact-band">
    <div class="contact-item contact-phone">
      <svg width="92" height="92" viewBox="0 0 92 92" aria-hidden="true">
        <rect x="3" y="3" width="86" height="86" rx="8" fill="none" stroke="var(--gold)" stroke-width="4"/>
        <path d="M24 20 L34 18 L40 32 L33 37 C37 47 44 54 54 58 L59 51 L73 57 L71 67 C69 72 64 74 58 72 C40 66 26 52 20 34 C18 28 19 23 24 20 Z" fill="none" stroke="var(--gold)" stroke-width="4" stroke-linejoin="round"/>
      </svg>
      <span>530-647-1185</span>
    </div>
    <div class="contact-item contact-email">
      <svg width="112" height="96" viewBox="0 0 112 96" aria-hidden="true">
        <path d="M62 70 H4 V8 H106 V48" fill="none" stroke="var(--gold)" stroke-width="4" stroke-linejoin="round"/>
        <path d="M4 8 L55 48 L106 8" fill="none" stroke="var(--gold)" stroke-width="4" stroke-linejoin="round"/>
        <circle cx="84" cy="70" r="20" fill="none" stroke="var(--gold)" stroke-width="4"/>
        <circle cx="84" cy="70" r="8" fill="none" stroke="var(--gold)" stroke-width="4"/>
        <path d="M92 62 V74 C92 80 100 80 103 74" fill="none" stroke="var(--gold)" stroke-width="4"/>
      </svg>
      <span>sales@brivolta.net</span>
    </div>
  </footer>
</main>
</body>
</html>
```